Commercial and Multifamily informational website

We need a website for our commercial real estate management company. We will manage offices, retail, apartments and others. Here is the brief verbiage: Providing quality commercial and multifamily portfolio management to Landlords, REITs, and financial institutions. 

Industry/Entity Type

Real Estate

Number of Pages Required

2 page

Font styles to use
Sans Serif
Other font styles liked:
• Muli, Garamond

Colors
0555a3
5c5c5c
3176b5
85acd3
474747

Requirements
Must have
• Home page and contact page

```html
<!DOCTYPE html>
<html lang="en">
<head>
<meta charset="utf-8">
<title>Norvale – Commercial &amp; Multifamily Portfolio Management</title>
<link href="https://fonts.googleapis.com/css2?family=Montserrat:wght@400;500;600&family=Roboto:wght@400;500&family=Open+Sans:wght@400&display=swap" rel="stylesheet">
<style>
:root{
  --navy:#053a7a;
  --brand:#0555a3;
  --brand-mid:#3176b5;
  --brand-light:#85acd3;
  --text:#5c5c5c;
  --text-dark:#474747;
  --band:#f5f5f5;
  --white:#ffffff;
}
*{box-sizing:border-box;margin:0;padding:0}
html,body{width:1200px;height:2956px;overflow:hidden;background:var(--white)}
body{position:relative;font-family:"Open Sans",sans-serif;color:var(--text)}
.abs{position:absolute}

/* top bar */
.topbar{left:0;top:0;width:1200px;height:28px;background:var(--navy);color:var(--white);font:500 10px "Roboto",sans-serif}
.social{left:98px;top:9px;display:flex;gap:10px}
.social span{width:9px;height:9px;border-radius:50%;background:var(--white);display:block}
.contact-info{right:98px;top:8px;display:flex;gap:26px}
.contact-info div{display:flex;align-items:center;gap:6px}

/* header */
.header{left:0;top:28px;width:1200px;height:94px;background:var(--white)}
.brand{left:98px;top:30px;display:flex;align-items:center;gap:10px;font:600 28px "Montserrat",sans-serif;color:var(--brand);letter-spacing:1px}
.brand i{width:14px;height:14px;background:var(--brand);display:block}
.nav{left:571px;top:0;height:94px;display:flex;font:500 14px "Montserrat",sans-serif;color:var(--text-dark)}
.nav a{display:flex;align-items:center;padding:0 24px;height:94px;color:inherit;text-decoration:none}
.nav a.active{background:var(--navy);color:var(--white);padding:0 14px;margin-right:8px}

/* hero */
.hero{left:0;top:122px;width:1200px;height:475px;background:linear-gradient(180deg,#7d8a98 0%,#5b6878 45%,#3d4756 100%)}
.hero h1{position:absolute;left:0;top:155px;width:1200px;text-align:center;font:600 30px/49px "Montserrat",sans-serif;color:var(--white);letter-spacing:1px;text-transform:uppercase}
.dots{left:574px;top:562px;display:flex;gap:4px}
.dots span{width:10px;height:10px;border-radius:50%;border:2px solid var(--white)}
.dots span.on{background:var(--white)}

/* sections */
.title{left:0;width:1200px;text-align:center;font:500 42px "Roboto",sans-serif;color:var(--navy)}
.lead{left:132px;width:936px;text-align:center;font:400 12.5px/21px "Open Sans",sans-serif;color:var(--text)}
.photo{background:linear-gradient(135deg,#dfe4ea,#b8c2cc)}
.label{font:500 18px "Montserrat",sans-serif;color:var(--navy);letter-spacing:1px}
.pager{left:1136px;top:950px;display:flex;flex-direction:column;gap:5px}
.pager span{width:10px;height:10px;border-radius:50%;border:2px solid var(--navy)}
.pager span.on{background:var(--navy)}

.band{left:0;top:1215px;width:1200px;height:436px;background:var(--band)}
.stat{width:200px;text-align:center}
.stat svg{display:block;margin:0 auto}
.stat .num{font:500 24px "Roboto",sans-serif;fill:var(--navy)}
.stat p{margin-top:24px;font:500 16px "Roboto",sans-serif;color:var(--brand);text-transform:uppercase}

.overlay-text{left:496px;top:2330px;width:605px;text-align:center;font:600 30px "Montserrat",sans-serif;color:var(--white);letter-spacing:1px}

.footer-art{left:0;top:2553px;width:1200px;height:378px;background:linear-gradient(90deg,#3f7fd0 0%,#dfe9f4 30%,#f4f7fb 50%,#dfe9f4 70%,#6b6fd6 100%)}
.footer-brand{left:0;top:2710px;width:1200px;text-align:center;font:600 44px "Montserrat",sans-serif;color:var(--brand);letter-spacing:2px}
.bottombar{left:0;top:2931px;width:1200px;height:25px;background:var(--navy);color:var(--white);font:500 11px/25px "Roboto",sans-serif;text-align:center}
</style>
</head>
<body>

<div class="abs topbar">
  <div class="abs social"><span></span><span></span><span></span><span></span><span></span></div>
  <div class="abs contact-info">
    <div><svg width="10" height="10" viewBox="0 0 10 10"><circle cx="5" cy="5" r="4" fill="none" stroke="#fff" stroke-width="1.4"/><path d="M5 2.5V5h2" stroke="#fff" stroke-width="1.2" fill="none"/></svg>Mon - Sat : 09.00 -19.00</div>
    <div><svg width="10" height="10" viewBox="0 0 10 10"><path d="M2 1h2l1 2.5-1.3 1a5 5 0 0 0 2 2l1-1.3L9 6v2a1 1 0 0 1-1 1A7 7 0 0 1 1 2a1 1 0 0 1 1-1z" fill="#fff"/></svg>+1 (555) 018 4421</div>
    <div><svg width="11" height="9" viewBox="0 0 11 9"><rect x="0" y="0" width="11" height="9" rx="1" fill="#fff"/><path d="M0.5 0.8l5 4 5-4" stroke="#053a7a" fill="none"/></svg>hello@norvale.example</div>
  </div>
</div>

<header class="abs header">
  <div class="abs brand"><i></i>NORVALE</div>
  <nav class="abs nav">
    <a class="active" href="#">Home</a><a href="#">About Us</a><a href="#">News</a><a href="#">Services</a><a href="#">Blog</a><a href="#">Contact</a>
  </nav>
</header>

<section class="abs hero" role="img" aria-label="Upward view of tall glass office towers against a cloudy sky">
  <h1>Providing quality commercial &amp; multifamily<br>portfolio management to landlords, REITs,<br>and financial institutions</h1>
</section>
<div class="abs dots"><span class="on"></span><span></span><span></span></div>

<h2 class="abs title" style="top:648px">WELCOME</h2>
<p class="abs lead" style="top:722px">Lorem Ipsum is simply dummy text of the printing and typesetting industry. Lorem Ipsum has been the industry's standard dummy text ever since the 1500s, when an unknown printer took a galley of type and scrambled it to make a type specimen book. It has survived not only five centuries, but also the leap into electronic typesetting, remaining essentially unchanged. It has survived not only five centuries, but also the leap into electronic</p>

<div class="abs photo" style="left:98px;top:829px;width:302px;height:290px" role="img" aria-label="Bright white open-plan office with desks and a plant"></div>
<div class="abs photo" style="left:449px;top:829px;width:301px;height:290px;background:linear-gradient(135deg,#e6e8ea,#a9adb3)" role="img" aria-label="Glass-fronted retail boutique interior with clothing racks"></div>
<div class="abs photo" style="left:800px;top:829px;width:301px;height:290px;background:linear-gradient(45deg,#8a6f6f,#e9d6b5 70%,#fff6e0)" role="img" aria-label="Apartment building facade in warm sunlight"></div>
<div class="abs label" style="left:98px;top:1136px">OFFICES</div>
<div class="abs label" style="left:449px;top:1136px">RETAIL</div>
<div class="abs label" style="left:800px;top:1134px">APARTMENTS</div>
<div class="abs pager"><span></span><span class="on"></span><span></span><span></span></div>

<div class="abs band"></div>
<h2 class="abs title" style="top:1262px;font-size:36px">WE DO IT ALL!</h2>
<p class="abs lead" style="top:1328px;left:150px;width:900px">Lorem Ipsum is simply dummy text of the printing and typesetting industry. Lorem Ipsum has been the industry's standard dummy text ever since the 1500s, when an unknown printer took a galley of type and scrambled it to make a type specimen book. It has survived not only five centuries, but also the leap into electronic typesetting, remaining essentially unchanged.</p>

<div class="abs stat" style="left:166px;top:1443px">
  <svg width="110" height="110" viewBox="0 0 110 110"><circle cx="55" cy="55" r="48" fill="none" stroke="var(--brand-light)" stroke-width="8"/><circle cx="55" cy="55" r="48" fill="none" stroke="var(--brand)" stroke-width="8" stroke-dasharray="256 302" transform="rotate(-90 55 55)"/><text class="num" x="55" y="63" text-anchor="middle">85%</text></svg>
  <p>Satisfied customers</p>
</div>
<div class="abs stat" style="left:402px;top:1443px">
  <svg width="110" height="110" viewBox="0 0 110 110"><circle cx="55" cy="55" r="48" fill="none" stroke="var(--brand-light)" stroke-width="8"/><circle cx="55" cy="55" r="48" fill="none" stroke="var(--brand)" stroke-width="8" stroke-dasharray="196 302" transform="rotate(-90 55 55)"/><text class="num" x="55" y="63" text-anchor="middle">65%</text></svg>
  <p>Partners</p>
</div>
<div class="abs stat" style="left:627px;top:1443px">
  <svg width="110" height="110" viewBox="0 0 110 110"><circle cx="55" cy="55" r="48" fill="none" stroke="var(--brand-light)" stroke-width="8"/><circle cx="55" cy="55" r="48" fill="none" stroke="var(--brand)" stroke-width="8" stroke-dasharray="284 302" transform="rotate(-90 55 55)"/><text class="num" x="55" y="63" text-anchor="middle">94%</text></svg>
  <p>Projects done</p>
</div>
<div class="abs stat" style="left:850px;top:1443px">
  <svg width="110" height="110" viewBox="0 0 110 110"><circle cx="55" cy="55" r="48" fill="none" stroke="var(--brand-light)" stroke-width="8"/><circle cx="55" cy="55" r="48" fill="none" stroke="var(--brand)" stroke-width="8" stroke-dasharray="272 302" transform="rotate(-90 55 55)"/><text class="num" x="55" y="63" text-anchor="middle">90%</text></svg>
  <p>Business plans</p>
</div>

<h2 class="abs title" style="top:1699px;font-size:34px">OUR PROJECS</h2>
<div class="abs photo" style="left:98px;top:1771px;width:375px;height:424px;background:linear-gradient(160deg,#6a4a3a,#e2a06a 45%,#8a8a92)" role="img" aria-label="Terrace lounge with sofas overlooking the sea at sunset"></div>
<div class="abs photo" style="left:98px;top:2218px;width:375px;height:306px;background:linear-gradient(180deg,#7fb0e0 0%,#b8c6b8 45%,#5e8f3e 100%)" role="img" aria-label="Suburban family house with front lawn and trees"></div>
<div class="abs photo" style="left:496px;top:1771px;width:605px;height:301px;background:linear-gradient(135deg,#f1f1f1,#c4c6c8)" role="img" aria-label="Modern white office interior with desk, chair and plants"></div>
<div class="abs photo" style="left:496px;top:2096px;width:605px;height:428px;background:linear-gradient(180deg,#5f8fc4,#9db4cc 60%,#7e8f7a)" role="img" aria-label="Modern glass office building under a blue sky"></div>
<svg class="abs" style="left:780px;top:2262px" width="36" height="36" viewBox="0 0 36 36"><circle cx="15" cy="15" r="10" fill="none" stroke="#fff" stroke-width="4"/><path d="M22 22l9 9" stroke="#fff" stroke-width="5" stroke-linecap="round"/></svg>
<div class="abs overlay-text">GET YOUR OFFICE NEW LOOK</div>

<div class="abs footer-art" role="img" aria-label="Colourful flat city skyline illustration with two cyclists"></div>
<div class="abs footer-brand">NORVALE</div>
<footer class="abs bottombar">© 2017 Norvale. All Rights Reserved.</footer>

</body>
</html>
```